Beauty website banner

We are an Australian beauty website selling mid and high end cosmetics and beauty products.

We need a banner that tells customers they can share their product wishlists with friends to let them know what they want for Christmas.

Target Market(s)

Female, 30-60, white collar

Industry/Entity Type

Cosmetics

Requirements
Must have
• 600 x 150 pixels in size

Words to be as follows, not including the (") of course.

"Share your wishlist with friends and family for Christmas!"

(Then in smaller font) "Just log in to your account, go to your wishlist and click on the ‘share wishlist’ button"

```html
<!DOCTYPE html>
<html lang="en">
<head>
<meta charset="utf-8">
<title>Share your Wishlist this Christmas</title>
<link rel="stylesheet" href="https://fonts.googleapis.com/css2?family=Cormorant+SC:wght@500;600&family=Pinyon+Script&display=swap">
<style>
  :root {
    --pink-pale: #ecd0db;
    --pink-soft: #dba6bb;
    --pink-mid: #c8608a;
    --pink-deep: #a82a62;
    --pink-dark: #8e1f52;
    --ink-burgundy: #5a1030;
    --accent-rose: #e56a9a;
    --white: #ffffff;
    --shadow: rgba(60, 0, 25, 0.75);
  }
  * { margin: 0; padding: 0; box-sizing: border-box; }
  html, body {
    width: 1200px;
    height: 300px;
    overflow: hidden;
    background: var(--white);
  }
  .banner {
    position: relative;
    width: 1200px;
    height: 300px;
    overflow: hidden;
  }
  .banner__ornament-field {
    position: absolute;
    inset: 0;
    background:
      radial-gradient(ellipse 420px 260px at 170px 150px, rgba(255,255,255,0.45), transparent 70%),
      radial-gradient(ellipse 380px 240px at 1000px 140px, rgba(150,20,80,0.35), transparent 75%),
      linear-gradient(90deg, var(--pink-pale) 0%, var(--pink-soft) 30%, var(--pink-mid) 52%, var(--pink-deep) 75%, var(--pink-dark) 100%);
  }
  .instructions {
    position: absolute;
    left: 124px;
    top: 92px;
    font-family: "Cormorant SC", "Times New Roman", serif;
    font-weight: 600;
    font-size: 17px;
    line-height: 28px;
    letter-spacing: 0.6px;
    color: var(--ink-burgundy);
  }
  .headline {
    font-family: "Pinyon Script", cursive;
    color: var(--white);
    font-weight: 400;
  }
  .headline span {
    position: absolute;
    white-space: nowrap;
    text-shadow: 2px 2px 3px var(--shadow);
  }
  .headline__share { left: 640px; top: 62px; font-size: 40px; }
  .headline__your {
    left: 728px; top: 66px; font-size: 24px;
    color: var(--accent-rose);
    text-shadow: none;
  }
  .headline__wishlist { left: 782px; top: 38px; font-size: 62px; }
  .headline__with { left: 656px; top: 120px; font-size: 20px; }
  .headline__friends { left: 698px; top: 100px; font-size: 40px; }
  .headline__for {
    left: 652px; top: 150px; font-size: 44px;
    color: var(--accent-rose);
    opacity: 0.55;
    text-shadow: none;
  }
  .headline__christmas { left: 678px; top: 140px; font-size: 62px; }
</style>
</head>
<body>
  <div class="banner">
    <div class="banner__ornament-field" role="img" aria-label="Layered pink and white floral, leaf and swirl ornaments across a rose gradient"></div>

    <p class="instructions">
      Just log in to your account,<br>
      go to your wishlist and click<br>
      on the ‘share wishlist’ button
    </p>

    <h1 class="headline">
      <span class="headline__share">Share</span>
      <span class="headline__your">your</span>
      <span class="headline__wishlist">Wishlist</span>
      <span class="headline__with">with</span>
      <span class="headline__friends">friends &amp; family</span>
      <span class="headline__for">for</span>
      <span class="headline__christmas">Christmas</span>
    </h1>
  </div>
</body>
</html>
```